Reggie Vosburn - Free Personalised Health Consultation - "Every body walks its own path"

This flyer will be left on tables/seats at speaking events and seminars and used to attain leads.

Top half will have "SMS me for a FREE Personalised Health Consultation" and my picture (see www.reggievosburn.example and pick most engaging photo) and underneath my contact details. It must have lines with "Notes:" halfway down so people can take notes at the seminar and lines on the back with my contact details again and "Notes: with lines.

I am having a business card also being designed by Plotnest for same and would like the flyer and business card to carry a similar feel/look for consistency.

Below is the brief for the business card being designed:
Business Card for www.reggievosburn.example site. It is a trust site and I use it for 1:1 relatable connections. It is the one I use for building intimate 1:1 trust building and Exec Coaching Services and programs for high wealth individuals and corporates. I also have a commercial programmatic site of my personal health products and services and programs for main stream one to many. www.crossgenvitality.example that can also provoke thought for the www.reggievosburn.example business card. (mind you will get a separate business card for that site, but want to provide context). It has a logo which you may want to draw from in designing the reggievosburn business card which is personal and is about building my brand. There is also a reggievosburn personal KX page and reggievosburn business KX page. I am a Certified Talent Compass 4.1 Coach with Verrick and you can get a corporate brief of me on there to give you more context https://www.verricktalenthub.example/coach/en-us/directory?search=reggie

Target Market(s)

Exec, IT, Health conscious. Corporates wanting to run Health and Wellness programs. Those wanting to go from good to great. Millennials to Middleaged.

Industry/Entity Type

Health And Wellness

Font styles to use
Sans Serif
Other font styles liked:
• Arial and Calibri ok too

Colors

Designer to choose colors to be used in the design.

Requirements
Must have
• Picture of me - use best from www.reggievosburn.example or can send one you choose.
• Contact details like my buisness card being designed by you guys in separate project.
• Name: Reggie Vosburn
• email: reggie@reggievosburn.,example
• Phone: Australia +61 455 318 026 Singapore: +65 8342 1960
Nice to have
• Open to ideas

```html
<!DOCTYPE html>
<html lang="en">
<head>
<meta charset="utf-8">
<title>Reggie Vosburn – Seminar Notes Flyer</title>
<link rel="stylesheet" href="https://fonts.googleapis.com/css2?family=Poppins:wght@400;500;700&family=Roboto:wght@500&display=swap">
<style>
  :root {
    --canvas-bg: #e4e4e4;
    --paper: #ffffff;
    --panel: #fbfbfb;
    --ink: #000000;
    --band-grey: #4a4b4b;
    --rule-grey: #9a9a9a;
    --photo-light: #d9d9d9;
    --photo-dark: #3a3a3a;
  }
  * { box-sizing: border-box; margin: 0; padding: 0; }
  html, body { width: 1200px; height: 1000px; overflow: hidden; }
  body {
    position: relative;
    background: var(--canvas-bg);
    font-family: "Poppins", Arial, sans-serif;
    color: var(--ink);
  }
  .flyer {
    position: absolute;
    width: 470px;
    height: 664px;
    background: var(--paper);
    overflow: hidden;
  }
  .flyer--front { left: 109px; top: 174px; }
  .flyer--back  { left: 608px; top: 176px; }

  /* Front hero */
  .hero { position: absolute; left: 0; top: 0; width: 470px; height: 322px; display: flex; }
  .hero__photo {
    width: 257px; height: 322px;
    background: linear-gradient(160deg, var(--photo-light) 0%, #a8a8a8 45%, var(--photo-dark) 100%);
  }
  .hero__panel {
    flex: 1;
    background: var(--panel);
    display: flex; flex-direction: column; align-items: center;
    padding-top: 62px;
  }
  .offer {
    font-weight: 700; font-size: 13px; line-height: 17px; text-align: center;
  }
  .name-tag {
    margin-top: 34px;
    width: 152px; height: 28px;
    background: var(--band-grey); color: var(--paper);
    font-family: "Roboto", Arial, sans-serif; font-weight: 500;
    font-size: 16px; line-height: 28px; text-align: center;
    white-space: nowrap;
  }
  .name-rule { width: 152px; height: 3px; background: var(--ink); margin-top: 8px; }
  .contact { font-size: 8.5px; line-height: 10.5px; text-align: center; font-weight: 500; white-space: nowrap; }
  .contact--phones { margin-top: 30px; }
  .contact--web { margin-top: 10px; }

  /* Notes */
  .notes-head {
    position: absolute; left: 0; width: 470px; height: 33px;
    color: var(--paper); font-weight: 700; font-size: 15px;
    line-height: 33px; text-align: center; letter-spacing: 0.3px;
  }
  .flyer--front .notes-head { top: 322px; background: var(--ink); }
  .flyer--back  .notes-head { top: 0; background: var(--band-grey); }
  .notes-lines {
    position: absolute; left: 0; width: 470px;
    background: repeating-linear-gradient(180deg, var(--paper) 0 19px, var(--rule-grey) 19px 20px);
  }
  .flyer--front .notes-lines { top: 355px; height: 280px; }
  .flyer--back  .notes-lines { top: 33px; height: 601px; }

  .footer-band { position: absolute; left: 0; bottom: 0; width: 470px; height: 29px; background: var(--band-grey); }
  .footer-contact {
    position: absolute; left: 0; bottom: 0; width: 470px; height: 30px;
    background: var(--ink); color: var(--paper);
    display: flex; justify-content: space-between; align-items: center;
    padding: 0 20px 0 23px;
    font-size: 9px; line-height: 10px;
  }
  .footer-contact__right { text-align: right; }
</style>
</head>
<body>
  <section class="flyer flyer--front">
    <div class="hero">
      <div class="hero__photo" role="img" aria-label="Black and white photo of Reggie Vosburn in a suit on a colonnaded veranda beside a bench and bicycle"></div>
      <div class="hero__panel">
        <p class="offer">SMS me for a FREE<br>Personalised Health<br>Consultation</p>
        <h1 class="name-tag">REGGIE VOSBURN</h1>
        <div class="name-rule"></div>
        <p class="contact contact--phones">Australia +61 455 318 026<br>Singapore: +65 8342 1960</p>
        <p class="contact contact--web">reggie@reggievosburn.example<br>www.reggievosburn.example</p>
      </div>
    </div>
    <h2 class="notes-head">NOTES</h2>
    <div class="notes-lines"></div>
    <div class="footer-band"></div>
  </section>

  <section class="flyer flyer--back">
    <h2 class="notes-head">NOTES</h2>
    <div class="notes-lines"></div>
    <div class="footer-contact">
      <p>Australia +61 455 318 026<br>Singapore: +65 8342 1960</p>
      <p class="footer-contact__right">reggie@reggievosburn.example<br>www.reggievosburn.example</p>
    </div>
  </section>
</body>
</html>
```